Recital Flyer - Here Comes Juniper Row

I need a flyer to depict a contemporary recital theme, "Here Comes Juniper Row..." for my 6th Annual Recital. I am looking for a Times Square "look" that is set in Detroit or has a "Detroit" Influence.

Here are some of the featured plays we are using: Lantern by the harbor, Quillbrook, A Velvet Tide, The Copper Kite, The Silent Orchard, Marigold Waltz, Verlanta, Kick Up Yo Dust/Kick Up Yo Soul, Ravelle The Musical, Skipjacket, Glint and more!
Updates

hi there I would like to add a $75 tip, how do I do that?

Target Market(s)

Dancers - students ages 3-15

Industry/Entity Type

Dance Studio

Font styles to use
Other font styles liked:
• Broadway or something familiar

Requirements
Must have
• My Logo and pertinent information on it:
• Date: June 24, 2017
• Time: 2 PM & 7 PM
• Location: Pinecrest Ridge High School
• 418 Tamsen Rd, Harrowfield Twp, MI 48512
Nice to have
• A New York (Times Square) flair with a gritty Detroit Influnce!

```html
<!DOCTYPE html>
<html lang="en">
<head>
<meta charset="utf-8">
<title>Recital Flyer – Here Comes Juniper Row</title>
<link rel="stylesheet" href="https://fonts.googleapis.com/css2?family=Berkshire+Swash&family=Cinzel:wght@700;900&display=swap">
<style>
  :root {
    --band: #d81b5f;
    --pink-light: #f8d3df;
    --pink-mid: #f28db0;
    --pink-deep: #ee5d8b;
    --title-ink: #2b2424;
    --script-ink: #c2185b;
    --white: #ffffff;
    --dancer-blue: #8fb8dc;
    --dancer-skin: #e8c4b4;
  }
  * { margin: 0; padding: 0; box-sizing: border-box; }
  html, body { width: 960px; height: 1200px; overflow: hidden; }
  body { background: var(--pink-deep); }
  .flyer {
    position: relative;
    width: 960px;
    height: 1200px;
    overflow: hidden;
    background: linear-gradient(180deg, var(--pink-light) 0%, var(--pink-mid) 42%, var(--pink-deep) 62%, var(--pink-deep) 100%);
  }
  .band-top {
    position: absolute; left: 0; top: 0; width: 100%; height: 14px;
    background: var(--band);
  }
  .band-bottom {
    position: absolute; left: 0; bottom: 0; width: 100%; height: 75px;
    background: var(--band);
  }
  .studio-name {
    position: absolute; top: 148px; left: 0; width: 100%;
    display: flex; justify-content: center; align-items: center; gap: 14px;
    font-family: "Cinzel", serif; font-weight: 700; font-size: 42px; line-height: 1;
    color: var(--title-ink); letter-spacing: 1px;
  }
  .studio-name .dot {
    width: 22px; height: 22px; border-radius: 50%; background: var(--title-ink);
  }
  .theme {
    position: absolute; top: 236px; left: 0; width: 100%;
    text-align: center;
    font-family: "Cinzel", serif; font-weight: 900; font-size: 50px; line-height: 1;
    color: var(--title-ink); letter-spacing: 0.5px;
  }
  .headline {
    position: absolute; left: 62px; top: 0;
    font-family: "Berkshire Swash", serif;
    color: var(--script-ink);
    text-shadow:
      -2px -2px 0 var(--white), 2px -2px 0 var(--white),
      -2px 2px 0 var(--white), 2px 2px 0 var(--white),
      0 3px 0 var(--white), 5px 6px 4px rgba(120, 10, 50, 0.45);
    line-height: 1;
  }
  .headline .line { position: absolute; left: 0; white-space: nowrap; }
  .line-for { top: 326px; font-size: 110px; }
  .line-num { top: 440px; font-size: 190px; }
  .line-annual { top: 630px; font-size: 112px; }
  .line-recital { top: 758px; font-size: 112px; }
  .rule {
    position: absolute; left: 66px; top: 917px; width: 502px; height: 3px;
    background: var(--white);
  }
  .details {
    position: absolute; left: 66px; top: 932px;
    list-style: none;
    font-family: "Cinzel", serif; font-weight: 700; font-size: 22px;
    color: var(--white); line-height: 45px;
  }
  .dancer {
    position: absolute; left: 490px; top: 330px; width: 440px; height: 850px;
  }
</style>
</head>
<body>
  <main class="flyer">
    <div class="band-top"></div>

    <div class="studio-name"><span class="dot"></span>Lumen Dance Studio LLC</div>

    <h1 class="theme">HERE COMES JUNIPER ROW...</h1>

    <div class="headline">
      <span class="line line-for">for my</span>
      <span class="line line-num">6th</span>
      <span class="line line-annual">Annual</span>
      <span class="line line-recital">Recital</span>
    </div>

    <div class="rule"></div>

    <ul class="details">
      <li>Date: June 24, 2017</li>
      <li>Time: 2 PM &amp; 7 PM</li>
      <li>Location: Pinecrest Ridge High School</li>
      <li>418 Tamsen Rd, Harrowfield Twp, MI 48512</li>
    </ul>

    <svg class="dancer" viewBox="0 0 440 850" role="img" aria-label="Photograph of a ballerina en pointe in a blue tutu, arms raised">
      <defs>
        <radialGradient id="dancerGlow" cx="50%" cy="50%" r="55%">
          <stop offset="0%" stop-color="#8fb8dc" stop-opacity="0.9"/>
          <stop offset="55%" stop-color="#e8c4b4" stop-opacity="0.45"/>
          <stop offset="100%" stop-color="#ee5d8b" stop-opacity="0"/>
        </radialGradient>
      </defs>
      <ellipse cx="235" cy="420" rx="215" ry="410" fill="url(#dancerGlow)"/>
      <ellipse cx="300" cy="838" rx="110" ry="10" fill="#a0144a" opacity="0.45"/>
    </svg>

    <div class="band-bottom"></div>
  </main>
</body>
</html>
```